Insert sheet for our Dog Food Package

We need an information sheet to go inn our pet food package, with branding, and information on ingredients, nutrition and feeding guidance. We will also need two additional items which will be a variation on the label design:
1) Label for package (detailed label about us and our food)
2) Label for outer shipping box (simple label for branding)
We will start with the information, insert page. The winning designer will then deliver the package and box labels as simplified versions of the same graphical theme.
I have attached samples of an earlier drafts of the insert piece. Please disregard the style, form and colors of the examples given. THEY ARE ONLY THERE TO SHOW WHAT INFORMATION SHOULD BE INCLUDED. All colors and style should be from our logo (attached). All graphics, font styles, and placement of elements need to be YOUR creative design - not a copy of the sample we gave. PLEASE READ THIS AND PLEASE DO NOT SUBMIT ANY VARIATION OF THE EXAMPLES!!!!!!!

Target Market(s)

Pet Owners

Industry/Entity Type

Pet Food

Colors
EB3D1F
EC4F4E
F09395
F8D3D4
FCEDEE

Requirements
Must have
• All new design. New colors (based in the palette of our logo), new graphics, new fonts, new placement of elements.
Should not have
• Please disregard the style, form and colors of the examples given. THEY ARE ONLY THERE TO SHOW WHAT INFORMATION SHOULD BE INCLUDED.

```html
<!DOCTYPE html>
<html lang="en">
<head>
<meta charset="utf-8">
<title>Kanu – Insert Sheet</title>
<link href="https://fonts.googleapis.com/css2?family=Fira+Sans+Extra+Condensed:wght@300;400;600;700&family=Antonio:wght@700&display=swap" rel="stylesheet">
<style>
  :root {
    --wine: #821619;
    --red: #a81f1d;
    --brown: #3c1a13;
    --frame: #c9b99a;
    --sand: #dcc7a3;
    --row: #e0d5c3;
    --white: #ffffff;
    --ink: #2a1612;
    --halo: #d99a7c;
    --art-top: #e9a35c;
    --art-bottom: #efdcc6;
  }
  * { margin: 0; padding: 0; box-sizing: border-box; }
  html, body { width: 965px; height: 1200px; overflow: hidden; background: var(--wine); }
  body { font-family: "Fira Sans Extra Condensed", "Arial Narrow", sans-serif; }
  .sheet { position: relative; width: 965px; height: 1200px; overflow: hidden; background: var(--wine); }
  .backdrop { position: absolute; inset: 0; }

  .artwork {
    position: absolute; left: 0; top: 570px; width: 473px; height: 630px;
    background: linear-gradient(165deg, var(--art-top) 0%, var(--art-bottom) 100%);
  }

  .card {
    position: absolute; background: var(--white);
    border: 6px solid var(--frame); border-radius: 34px; overflow: hidden;
  }
  .card-head {
    background: var(--brown); color: var(--white); font-weight: 600;
    text-align: center; border-radius: 0 0 6px 6px;
  }
  .card-title { color: var(--red); font-weight: 700; text-align: center; }

  .nutrition { left: 49px; top: 71px; width: 416px; height: 422px; }
  .nutrition .card-head { height: 67px; font-size: 28px; line-height: 67px; }
  .nutrition .card-title { font-size: 29px; line-height: 34px; margin-top: 10px; }
  .facts {
    display: grid; grid-template-columns: 1fr auto; margin: 3px 29px 0 27px;
    font-size: 24.5px; font-weight: 600; color: var(--ink); line-height: 28px;
  }
  .facts span:nth-child(even) { text-align: right; }
  .ingredients {
    margin: 18px 20px 0 27px; font-size: 21.3px; font-weight: 300;
    line-height: 27.3px; color: var(--ink); white-space: nowrap;
  }

  .brand {
    position: absolute; left: 527px; top: 75px; width: 264px; height: 264px;
    border-radius: 50%; background: var(--halo); opacity: .92;
    display: flex; align-items: center; justify-content: center; flex-direction: column;
    color: var(--white);
  }
  .brand-name { font-size: 58px; font-weight: 700; letter-spacing: 6px; line-height: 1; }
  .brand-line { font-size: 20px; font-weight: 700; letter-spacing: 3px; margin-top: 6px; }

  .story { position: absolute; right: 76px; top: 358px; width: 380px; text-align: right; }
  .story-title {
    font-family: "Antonio", "Arial Narrow", sans-serif; font-weight: 700;
    font-size: 74px; color: var(--white); line-height: 80px;
  }
  .story-lead {
    margin-top: 16px; font-size: 22.5px; font-weight: 600; color: var(--sand);
    line-height: 27.4px; white-space: nowrap;
  }
  .story-body {
    position: absolute; right: 87px; top: 582px; width: 380px; text-align: right;
    font-size: 17px; font-weight: 600; color: var(--white); line-height: 21.4px; white-space: nowrap;
  }

  .feeding { left: 473px; top: 736px; width: 416px; height: 420px; }
  .feeding .card-head { height: 66px; font-size: 28px; line-height: 66px; }
  .feeding .card-title { font-size: 29px; line-height: 34px; margin-top: 10px; }
  .plan-head {
    display: grid; grid-template-columns: 238px 120px; margin-top: 4px;
    font-size: 23px; font-weight: 700; color: var(--ink); line-height: 26.5px; text-align: center;
  }
  .plan { position: absolute; left: 26px; top: 192px; width: 353px; border-collapse: collapse; }
  .plan td { height: 29px; font-size: 18px; font-weight: 300; color: var(--ink); padding: 0; }
  .plan td:first-child { padding-left: 63px; }
  .plan td:last-child { padding-left: 92px; }
  .plan tr:nth-child(odd) td { background: var(--row); }
  .plan tr.ruled td { border-top: 1.5px solid var(--brown); }
</style>
</head>
<body>
<main class="sheet">
  <svg class="backdrop" width="965" height="1200" viewBox="0 0 965 1200" aria-hidden="true">
    <polygon points="721,0 965,0 965,1200 238,1200" fill="var(--red)"/>
  </svg>

  <div class="artwork" role="img"
       aria-label="Illustration of a smiling orange and cream dog peeking up with a raised paw, surrounded by floating hearts"></div>

  <section class="card nutrition">
    <h2 class="card-head">We prepare the best for Shadow</h2>
    <h3 class="card-title">NUTRITION INFORMATION</h3>
    <div class="facts">
      <span>Protein: 15%</span><span>Total Fat: 9.5%</span>
      <span>Crude Fiber: 2.0%</span><span>Moisture: 72%</span>
    </div>
    <p class="ingredients">Potassium Citrate, DiCalcium Phosphate,<br>Calcium Carbonate, Garbanzo Beans, Choline<br>Bitartrate, Taurine, Salt, Zinc Proteinate,<br>Magnesium Oxide, Iron Proteinate, Vitamin<br>B-12, Selenium, Niacin, Riboflavin, Calcium<br>Panthothenate, Thiamine, Vitamin A, Vitamin D,<br>Calcium Iodate, Vitamon B6m Folic Acid.</p>
  </section>

  <div class="brand">
    <span class="brand-name">KANU</span>
    <span class="brand-line">THE WHOLE HOUND</span>
  </div>

  <section class="story">
    <h1 class="story-title">OUR STORY</h1>
    <p class="story-lead">We Revolutionized the industry. Not<br>Formulated to meet a minimum<br>standard, but to develop the<br>maximum health of the whole dog.</p>
  </section>
  <p class="story-body">We didn’t just set about to create a food that will<br>‘pass a minimum standard’. We set out to<br>revolutionize the industryu by creating a food that<br>is designed with Superfoods, Wholesome Grains,<br>and Powerful Oils to help your dog achieve their<br>maximum health, happiness and longetivity.</p>

  <section class="card feeding">
    <h2 class="card-head">How much shuld I feed Shadow?</h2>
    <h3 class="card-title">RECOMMENDED FEEDING PLAN</h3>
    <div class="plan-head"><span>APPROXIMATE<br>WEIGHT</span><span>FULL MEAL</span></div>
    <table class="plan">
      <tr class="ruled"><td>&lt;20 lbs</td><td>110 g</td></tr>
      <tr class="ruled"><td>20 -29 lbs</td><td>200 g</td></tr>
      <tr><td>30-39 lbs</td><td>250 g</td></tr>
      <tr><td>40-54 lbs</td><td>300 g</td></tr>
      <tr class="ruled"><td>55-69 lbs</td><td>350 g</td></tr>
      <tr><td>70-85 lbs</td><td>400 g</td></tr>
      <tr class="ruled"><td>85+ lbs</td><td>500 g</td></tr>
    </table>
  </section>
</main>
</body>
</html>
```